Brisa Pastry Mill Business card

We are empanada whole-sellers and I want a business card design with a picture of an empanada on it that also mentions first trial order FREE. our contact number 555-214-7093 our website www.brisapastry.example and business email Tobin@brisapastry.example

If you want any of our artwork please feel free to email me at the address above.

```html
<!DOCTYPE html>
<html lang="en">
<head>
<meta charset="utf-8">
<title>Brisa Pastry Mill – Business Card</title>
<link rel="stylesheet" href="https://fonts.googleapis.com/css2?family=Bree+Serif&display=swap">
<style>
  :root {
    --ink: #111111;
    --sun: #f7d21a;
    --sun-deep: #f0a800;
    --mustard: #e5b62a;
    --mustard-light: #f0c93f;
    --pastry: #e7a53a;
    --pastry-light: #f6d27a;
    --paper: #ffffff;
    --stage: #f2f2f0;
  }
  * { margin: 0; padding: 0; box-sizing: border-box; }
  html, body {
    width: 1200px; height: 873px; overflow: hidden;
    background: var(--stage);
    font-family: "Bree Serif", Georgia, serif;
  }
  .canvas { position: relative; width: 1200px; height: 873px; }
  .card {
    position: absolute; top: 282px;
    width: 540px; height: 309px; overflow: hidden;
    border-radius: 4px;
    box-shadow: 0 10px 28px rgba(0,0,0,.18);
  }
  /* Front */
  .card--front { left: 40px; background: linear-gradient(135deg, var(--sun) 20%, var(--sun-deep) 100%); }
  .front-wave { position: absolute; inset: 0; }
  .brand-block { position: absolute; left: 150px; top: 34px; width: 340px; text-align: center; color: var(--ink); }
  .brand-name { font-size: 38px; line-height: 1; }
  .brand-tag { font-size: 13.5px; letter-spacing: .5px; margin-top: 8px; }
  .brand-rule { height: 2px; background: var(--ink); width: 220px; margin: 7px auto 5px; }
  .brand-offer { font-size: 18px; letter-spacing: 1px; }
  .dish-badge {
    position: absolute; left: 412px; top: 168px; width: 96px; height: 96px;
    border-radius: 50%; background: var(--paper); border: 4px solid var(--sun);
    display: flex; align-items: center; justify-content: center;
  }
  .dish-photo {
    width: 70px; height: 50px; border-radius: 50% 50% 45% 45%;
    background: radial-gradient(circle at 45% 40%, var(--pastry-light), var(--pastry));
  }
  .contact { position: absolute; color: var(--sun); font-size: 14px; line-height: 1.6; }
  .card--front .contact { left: 26px; bottom: 20px; }
  .contact-row { display: flex; align-items: center; gap: 7px; }
  .dot { width: 9px; height: 9px; border-radius: 50%; background: var(--sun); }
  .phone-icon { width: 12px; height: 12px; }
  /* Back */
  .card--back { left: 620px; background: linear-gradient(160deg, var(--mustard-light), var(--mustard)); }
  .back-pattern { position: absolute; inset: 0 0 72px 0; background: linear-gradient(180deg, rgba(255,255,255,.08), rgba(0,0,0,.04)); }
  .card--back .brand-block { left: 0; width: 540px; top: 24px; }
  .card--back .brand-name { font-size: 40px; }
  .card--back .brand-offer { font-size: 16px; margin-top: 6px; }
  .card--back .dish-photo {
    position: absolute; left: 215px; top: 140px; width: 110px; height: 76px;
  }
  .back-band { position: absolute; left: 0; bottom: 0; width: 540px; height: 82px; }
  .card--back .contact {
    left: 0; width: 540px; bottom: 12px; font-size: 13px; line-height: 1.7;
  }
  .contact-line { display: flex; justify-content: center; gap: 20px; }
</style>
</head>
<body>
<main class="canvas">
  <section class="card card--front">
    <svg class="front-wave" viewBox="0 0 540 309" aria-hidden="true">
      <path d="M0,0 L95,0 C120,60 90,120 150,160 C230,210 330,190 400,170 C380,220 420,275 540,280 L540,309 L0,309 Z" fill="var(--ink)"/>
    </svg>
    <div class="brand-block">
      <div class="brand-name">Brisa Pastry Mill</div>
      <div class="brand-tag">EMPANADA WHOLESALERS</div>
      <div class="brand-rule"></div>
      <div class="brand-offer">FIRST TRIAL ORDER FREE</div>
    </div>
    <div class="dish-badge"><div class="dish-photo" role="img" aria-label="Photo of a golden baked empanada"></div></div>
    <div class="contact">
      <div class="contact-row"><span class="dot"></span>@brisapastry</div>
      <div class="contact-row">
        <svg class="phone-icon" viewBox="0 0 24 24" aria-hidden="true"><path fill="var(--sun)" d="M6.6 10.8a15.1 15.1 0 0 0 6.6 6.6l2.2-2.2c.3-.3.7-.4 1-.2 1.1.4 2.3.6 3.6.6.6 0 1 .4 1 1V20c0 .6-.4 1-1 1A17 17 0 0 1 3 4c0-.6.4-1 1-1h3.5c.6 0 1 .4 1 1 0 1.3.2 2.5.6 3.6.1.3 0 .7-.2 1z"/></svg>
        555-214-7093
      </div>
      <div class="contact-row">www.brisapastry.example</div>
      <div class="contact-row">Tobin@brisapastry.example</div>
    </div>
  </section>

  <section class="card card--back">
    <div class="back-pattern" role="img" aria-label="Subtle diamond lattice pattern"></div>
    <div class="brand-block">
      <div class="brand-name">Brisa Pastry Mill</div>
      <div class="brand-tag">EMPANADA WHOLESALERS</div>
      <div class="brand-offer">FIRST TRIAL ORDER FREE</div>
    </div>
    <div class="dish-photo" role="img" aria-label="Photo of a golden baked empanada"></div>
    <svg class="back-band" viewBox="0 0 540 82" preserveAspectRatio="none" aria-hidden="true">
      <polygon fill="var(--ink)" points="0,12 9,4 18,12 27,4 36,12 45,4 54,12 63,4 72,12 81,4 90,12 99,4 108,12 117,4 126,12 135,4 144,12 153,4 162,12 171,4 180,12 189,4 198,12 207,4 216,12 225,4 234,12 243,4 252,12 261,4 270,12 279,4 288,12 297,4 306,12 315,4 324,12 333,4 342,12 351,4 360,12 369,4 378,12 387,4 396,12 405,4 414,12 423,4 432,12 441,4 450,12 459,4 468,12 477,4 486,12 495,4 504,12 513,4 522,12 531,4 540,12 540,82 0,82"/>
    </svg>
    <div class="contact">
      <div class="contact-line">
        <span class="contact-row"><span class="dot"></span>@brisapastry</span>
        <span class="contact-row">
          <svg class="phone-icon" viewBox="0 0 24 24" aria-hidden="true"><path fill="var(--sun)" d="M6.6 10.8a15.1 15.1 0 0 0 6.6 6.6l2.2-2.2c.3-.3.7-.4 1-.2 1.1.4 2.3.6 3.6.6.6 0 1 .4 1 1V20c0 .6-.4 1-1 1A17 17 0 0 1 3 4c0-.6.4-1 1-1h3.5c.6 0 1 .4 1 1 0 1.3.2 2.5.6 3.6.1.3 0 .7-.2 1z"/></svg>
          555-214-7093
        </span>
      </div>
      <div class="contact-line">
        <span>www.brisapastry.example</span>
        <span>Tobin@brisapastry.example</span>
      </div>
    </div>
  </section>
</main>
</body>
</html>
```